First of a series of workplace posters- our values statement

To produce a high quality poster of our values, we would like one in a3 and one in a4 both full colour
By utilising the supplied text , the intent is to produce a really striking poster for all our work places, which set out our company values. we are looking for really strong graphical elements which support the message visually . This will be the first of a series of posters, so we are looking to establish at stylistic theme for all with this one. for more on our business,

Target Market(s)

Internal and external audiences, our clients are all tier one companies

Requirements
Must have
• contemporary design rather than conservative, visually striking
• Must be clearly readable from a reasonable distance
Nice to have
• would be nice to tie in to the blue and greens of our logo in similar fashion to our website. www.qrtbuildwise.com
Should not have
• Difficult to read fonts,

```html
<!DOCTYPE html>
<html lang="en">
<head>
<meta charset="utf-8">
<title>Our Values – We value our people</title>
<link href="https://fonts.googleapis.com/css2?family=Montserrat:wght@500;600;700&display=swap" rel="stylesheet">
<style>
  :root {
    --navy: #053069;
    --green: #6cb120;
    --white: #ffffff;
  }
  * { margin: 0; padding: 0; box-sizing: border-box; }
  html, body { width: 848px; height: 1200px; overflow: hidden; background: var(--navy); }
  .poster {
    position: relative;
    width: 848px;
    height: 1200px;
    background: var(--navy);
    font-family: "Montserrat", Arial, sans-serif;
    color: var(--white);
    overflow: hidden;
  }
  .hero-mark { position: absolute; left: 236px; top: 78px; width: 380px; height: 164px; }
  .headline {
    position: absolute;
    top: 300px;
    width: 100%;
    text-align: center;
    font-weight: 700;
    font-size: 49px;
    line-height: 58px;
    letter-spacing: 0.2px;
  }
  .headline .accent { color: var(--green); }
  .intro {
    position: absolute;
    top: 451px;
    width: 100%;
    text-align: center;
    font-weight: 600;
    font-size: 19.5px;
  }
  .value { position: absolute; display: flex; align-items: center; }
  .value-icon { flex: none; fill: var(--green); stroke: var(--green); }
  .value-text {
    font-weight: 500;
    font-size: 17.5px;
    line-height: 27px;
  }
  .corner { position: absolute; right: 0; bottom: 0; width: 290px; height: 160px; }
  .brand {
    position: absolute;
    right: 42px;
    bottom: 46px;
    display: flex;
    align-items: center;
    gap: 8px;
    color: var(--navy);
    font-weight: 700;
    font-size: 20px;
  }
  .brand-dot { width: 14px; height: 14px; border-radius: 50%; background: var(--green); }
</style>
</head>
<body>
<main class="poster">
  <svg class="hero-mark" viewBox="0 0 380 164" aria-hidden="true">
    <path d="M26 32 Q0 82 26 122" fill="none" stroke="#6cb120" stroke-width="9" stroke-linecap="round"/>
    <path d="M354 32 Q380 82 354 122" fill="none" stroke="#6cb120" stroke-width="9" stroke-linecap="round"/>
    <circle cx="192" cy="15" r="13" fill="#fff"/>
    <path d="M168 34 H216 Q222 34 222 40 V96 Q222 102 216 102 H212 L207 162 H177 L172 102 H168 Q162 102 162 96 V40 Q162 34 168 34 Z" fill="#fff"/>
  </svg>

  <h1 class="headline">We value our <span class="accent">people</span><br>above everything else</h1>
  <p class="intro">We demonstrate this by:</p>

  <div class="value" style="left:74px; top:543px;">
    <svg class="value-icon" width="60" height="54" viewBox="0 0 60 54" style="margin-right:32px"><path d="M30 52 C12 38 2 28 2 16 C2 7 9 1 17 1 C23 1 27 5 30 9 C33 5 37 1 43 1 C51 1 58 7 58 16 C58 28 48 38 30 52 Z" stroke="none"/></svg>
    <p class="value-text">Providing safe, positive,<br>enjoyable workplaces<br>where everyone feels<br>valued and respected</p>
  </div>

  <div class="value" style="left:457px; top:545px;">
    <svg class="value-icon" width="60" height="64" viewBox="0 0 60 64" style="margin-right:33px"><path d="M0 64 V50 H15 V35 H30 V20 H45 V3 H60 V64 Z" stroke="none"/></svg>
    <p class="value-text">Providing careers,<br>not jobs, we grow<br>together.</p>
  </div>

  <div class="value" style="left:51px; top:706px;">
    <svg class="value-icon" width="90" height="82" viewBox="0 0 90 82" style="margin-right:25px">
      <line x1="40" y1="38" x2="40" y2="52" stroke-width="2.5"/>
      <line x1="40" y1="52" x2="18" y2="64" stroke-width="2.5"/>
      <line x1="40" y1="52" x2="68" y2="58" stroke-width="2.5"/>
      <circle cx="40" cy="52" r="4.5" stroke="none"/>
      <circle cx="40" cy="7" r="7" stroke="none"/><path d="M26 36 V26 Q26 17 35 17 H45 Q54 17 54 26 V36 Z" stroke="none"/>
      <circle cx="14" cy="53" r="7" stroke="none"/><path d="M0 82 V72 Q0 63 9 63 H19 Q28 63 28 72 V82 Z" stroke="none"/>
      <circle cx="73" cy="47" r="7" stroke="none"/><path d="M59 76 V66 Q59 57 68 57 H78 Q87 57 87 66 V76 Z" stroke="none"/>
    </svg>
    <p class="value-text">Encouraging inclusion,<br>participation and<br>collaboration.</p>
  </div>

  <div class="value" style="left:478px; top:714px;">
    <svg class="value-icon" width="56" height="90" viewBox="0 0 56 90" style="margin-right:17px">
      <path d="M14 48 L2 80 L13 76 L19 88 L28 58 Z M42 48 L54 80 L43 76 L37 88 L28 58 Z" stroke="none"/>
      <circle cx="28" cy="28" r="27" stroke="none"/>
      <circle cx="28" cy="28" r="17" fill="#053069" stroke="none"/>
      <circle cx="28" cy="28" r="11" stroke="none"/>
      <path d="M28 21 L30 26 L35 26 L31 29 L33 34 L28 31 L23 34 L25 29 L21 26 L26 26 Z" fill="#053069" stroke="none"/>
    </svg>
    <p class="value-text">Recognising and<br>rewarding contribution<br>and excellence.</p>
  </div>

  <div class="value" style="left:57px; top:884px;">
    <svg class="value-icon" width="88" height="76" viewBox="0 0 88 76" style="margin-right:22px">
      <circle cx="44" cy="6" r="6" stroke="none"/>
      <path d="M37 14 H51 V36 H48 L47 48 H41 L40 36 H37 Z" stroke="none"/>
      <path d="M4 18 L12 20 Q10 40 22 56 Q30 64 40 64 V76 H20 Q6 66 2 48 Q0 32 4 18 Z" stroke="none"/>
      <path d="M84 18 L76 20 Q78 40 66 56 Q58 64 48 64 V76 H68 Q82 66 86 48 Q88 32 84 18 Z" stroke="none"/>
      <path d="M14 18 L20 30 M74 18 L68 30" stroke-width="4" stroke-linecap="round"/>
    </svg>
    <p class="value-text">Supporting our people<br>through tough times.</p>
  </div>

  <div class="value" style="left:460px; top:896px;">
    <svg class="value-icon" width="74" height="70" viewBox="0 0 74 70" style="margin-right:15px">
      <rect x="33" y="4" width="8" height="58" stroke="none"/>
      <rect x="22" y="62" width="30" height="7" rx="2" stroke="none"/>
      <rect x="6" y="9" width="62" height="6" rx="2" stroke="none"/>
      <circle cx="37" cy="5" r="5" stroke="none"/>
      <path d="M12 15 L3 35 M12 15 L21 35 M62 15 L53 35 M62 15 L71 35" stroke-width="1.5" fill="none"/>
      <path d="M1 35 H23 Q21 44 12 44 Q3 44 1 35 Z M51 35 H73 Q71 44 62 44 Q53 44 51 35 Z" stroke="none"/>
    </svg>
    <p class="value-text">Fostering healthy<br>work life balance.</p>
  </div>

  <svg class="corner" viewBox="0 0 290 160" preserveAspectRatio="none" aria-hidden="true">
    <path d="M0 160 Q60 20 290 8 V160 Z" fill="#fff"/>
  </svg>
  <div class="brand"><span class="brand-dot"></span>QRT Buildwise</div>
</main>
</body>
</html>
```